Cutting Board Oil and Finish

I designed these two labels and I am now wanting something a little more professional looking. The label should catch your eye, be unique but also professional. The design can also play off some of the ingredients too if you think that might look good ( beeswax, lemon oil, orange oil) I need two labels: One will be for the bottle of oil and the other will be for the bottle of finish. They are both the same brand so both labels should have the same theme and look related. The dimensions of the label for the bottle of oil will be 4 x 2.25 inches. The dimensions for the bottle of finish will be 3 x 2.125 inches
Target Market(s)
Anyone who uses cutting boards: moms, dads, chefs, woodworkers etc
Industry/Entity Type
It Professional
Look and feel

```html
<!DOCTYPE html>
<html lang="en">
<head>
<meta charset="utf-8">
<title>Cutting Board Finish Label</title>
<link href="https://fonts.googleapis.com/css2?family=Rosario:wght@400;600;700&display=swap" rel="stylesheet">
<style>
  :root {
    --rust: #a65228;
    --frame: #6b3520;
    --brown-deep: #5e2f1c;
    --brown-mid: #8a4a26;
    --orange-light: #e49440;
    --orange-base: #cf6a22;
    --wood-light: #f3dcb8;
    --wood-red: #b85a3a;
    --white: #ffffff;
  }
  html, body {
    margin: 0;
    padding: 0;
    width: 1200px;
    height: 889px;
    overflow: hidden;
    background: var(--white);
  }
  .label {
    display: block;
    width: 1200px;
    height: 889px;
  }
  .label text {
    font-family: "Rosario", sans-serif;
  }
  .brand-name {
    fill: var(--brown-deep);
    font-weight: 700;
    font-size: 68px;
    letter-spacing: 1px;
  }
  .size-mark {
    fill: var(--white);
    font-size: 34px;
    letter-spacing: 1px;
  }
  .product-title {
    fill: var(--white);
    font-size: 92px;
  }
  .ingredients {
    fill: var(--white);
    font-size: 41px;
  }
  .tagline {
    fill: var(--white);
    font-size: 31px;
  }
</style>
</head>
<body>
<svg class="label" viewBox="0 0 1200 889" xmlns="http://www.w3.org/2000/svg">
  <defs>
    <radialGradient id="panel-glow" cx="600" cy="560" r="700" gradientUnits="userSpaceOnUse">
      <stop offset="0" stop-color="var(--orange-light)"/>
      <stop offset="1" stop-color="var(--orange-base)"/>
    </radialGradient>
    <linearGradient id="banner-fill" x1="0" y1="0" x2="1" y2="0">
      <stop offset="0" stop-color="var(--frame)"/>
      <stop offset="0.5" stop-color="var(--brown-mid)"/>
      <stop offset="1" stop-color="var(--frame)"/>
    </linearGradient>
    <linearGradient id="tail-left-fill" x1="0" y1="0" x2="1" y2="0">
      <stop offset="0" stop-color="var(--rust)"/>
      <stop offset="1" stop-color="var(--frame)"/>
    </linearGradient>
    <linearGradient id="tail-right-fill" x1="1" y1="0" x2="0" y2="0">
      <stop offset="0" stop-color="var(--rust)"/>
      <stop offset="1" stop-color="var(--frame)"/>
    </linearGradient>
    <linearGradient id="board-fill" x1="0" y1="0" x2="1" y2="0.4">
      <stop offset="0" stop-color="var(--wood-light)"/>
      <stop offset="0.5" stop-color="var(--wood-red)"/>
      <stop offset="1" stop-color="var(--wood-light)"/>
    </linearGradient>
  </defs>

  <!-- label base and framed panel -->
  <rect class="label-base" x="0" y="0" width="1200" height="889" rx="42" fill="var(--rust)"/>
  <rect class="label-panel" x="74" y="74" width="1050" height="734" rx="40" fill="url(#panel-glow)" stroke="var(--frame)" stroke-width="7"/>

  <!-- brand -->
  <text class="brand-name" x="600" y="170" text-anchor="middle">HARLOW'S</text>
  <text class="size-mark" x="1022" y="246" text-anchor="middle">8 OZ</text>

  <!-- product illustration area -->
  <g class="board-illustration" role="img" aria-label="Striped wooden cutting board with a handle slot">
    <polygon points="290,272 478,192 835,258 662,556 540,548" fill="url(#board-fill)"/>
  </g>

  <!-- title ribbon -->
  <g class="title-ribbon">
    <polygon class="ribbon-tail" points="184,352 394,352 394,586 224,590 262,470" fill="url(#tail-left-fill)" stroke="var(--white)" stroke-width="8" stroke-linejoin="miter"/>
    <polygon class="ribbon-tail" points="1016,352 806,352 806,586 976,590 938,470" fill="url(#tail-right-fill)" stroke="var(--white)" stroke-width="8" stroke-linejoin="miter"/>
    <polygon class="ribbon-fold" points="394,528 394,586 300,586" fill="var(--brown-deep)"/>
    <polygon class="ribbon-fold" points="806,528 806,586 900,586" fill="var(--brown-deep)"/>
    <path class="ribbon-face" d="M266,292 Q600,282 934,292 L934,530 Q600,520 266,530 Z" fill="url(#banner-fill)" stroke="var(--white)" stroke-width="10"/>
    <text class="product-title" x="600" y="384" text-anchor="middle">Cutting</text>
    <text class="product-title" x="600" y="488" text-anchor="middle">Board Finish</text>
  </g>

  <!-- ingredients and claim -->
  <text class="ingredients" x="600" y="648" text-anchor="middle">Mineral oil, Beeswax, Carnauba wax,</text>
  <text class="ingredients" x="600" y="706" text-anchor="middle">Orange oil, and Lemon oil</text>
  <text class="tagline" x="600" y="774" text-anchor="middle">All-Natural Food-Safe Finish for All typs of Woodware</text>
</svg>
</body>
</html>
```